Brindlewood Terrain, LLC Business Card Updates
Oil and Gas Land Services/ A Full Service Land Management Company/ Mineral Owner Consultation and Re
Use same font as used in my logo
Gavin Ressler
Petroleum Landman
426 West Orchard Lane
North Canton, OH 44720
gavin.r.ressler@quellmail.net
No website on this

```html
<!DOCTYPE html>
<html lang="en">
<head>
<meta charset="utf-8">
<title>Brindlewood Terrain, LLC – Business Card</title>
<link rel="stylesheet" href="https://fonts.googleapis.com/css2?family=Oswald:wght@400;500&family=Open+Sans:wght@400;600&display=swap">
<style>
  :root {
    --page-bg: #e9e9e9;
    --card-dark: #3b3b3b;
    --card-light: #ffffff;
    --card-mist: #ececec;
    --ink-dark: #333333;
    --ink-light: #f2f2f2;
    --ink-muted: #bdbdbd;
    --accent-line: #8a8a8a;
  }
  * { box-sizing: border-box; margin: 0; padding: 0; }
  html, body { width: 1200px; height: 980px; overflow: hidden; }
  body {
    background: var(--page-bg);
    display: flex;
    flex-direction: column;
    align-items: center;
    justify-content: center;
    gap: 56px;
    font-family: "Open Sans", Arial, sans-serif;
  }
  .card {
    position: relative;
    width: 760px;
    height: 434px;
    border-radius: 22px;
    overflow: hidden;
    box-shadow: 0 6px 18px rgba(0,0,0,0.18);
  }

  /* Back */
  .card-back {
    background: var(--card-dark);
    display: flex;
    align-items: center;
    justify-content: center;
  }
  .back-brand {
    display: flex;
    align-items: center;
    gap: 16px;
    font-family: "Oswald", Arial, sans-serif;
    font-weight: 500;
    font-size: 40px;
    letter-spacing: 3px;
    text-transform: uppercase;
    color: var(--ink-light);
  }
  .brand-square {
    width: 18px; height: 18px;
    background: var(--ink-light);
  }

  /* Front */
  .card-front { background: var(--card-light); }
  .front-waves { position: absolute; inset: 0; width: 100%; height: 100%; }
  .front-brand {
    position: absolute;
    top: 50px;
    left: 0; right: 0;
    text-align: center;
    font-family: "Oswald", Arial, sans-serif;
    color: var(--ink-dark);
  }
  .front-brand .brand-name {
    font-weight: 500;
    font-size: 46px;
    letter-spacing: 3px;
    text-transform: uppercase;
    line-height: 1.1;
  }
  .front-brand .brand-tagline {
    margin-top: 6px;
    font-family: "Open Sans", Arial, sans-serif;
    font-size: 19px;
    letter-spacing: 1.5px;
  }
  .contact-list {
    position: absolute;
    left: 36px;
    bottom: 30px;
    list-style: none;
    color: var(--ink-light);
    font-size: 13.5px;
    line-height: 1.5;
  }
  .contact-list li { display: flex; align-items: center; gap: 10px; margin-top: 4px; }
  .contact-icon { width: 16px; height: 16px; flex: none; }
  .contact-lines { display: block; }
  .person {
    position: absolute;
    right: 40px;
    bottom: 32px;
    text-align right;
    text-align: right;
    color: var(--ink-light);
  }
  .person-name {
    font-family: "Oswald", Arial, sans-serif;
    font-size: 22px;
    letter-spacing: 2px;
    text-transform: uppercase;
  }
  .person-title {
    font-size: 14px;
    letter-spacing: 2px;
    text-transform: uppercase;
    color: var(--ink-muted);
  }
</style>
</head>
<body>

  <section class="card card-back" aria-label="Card back">
    <div class="back-brand"><span class="brand-square"></span>Brindlewood Terrain</div>
  </section>

  <section class="card card-front" aria-label="Card front">
    <svg class="front-waves" viewBox="0 0 760 434" preserveAspectRatio="none" aria-hidden="true">
      <path d="M0 192 C 200 172, 360 272, 520 292 C 640 307, 710 292, 760 282 L760 434 L0 434 Z" fill="var(--card-mist)"/>
      <path d="M0 220 C 200 200, 360 300, 520 320 C 640 335, 710 320, 760 310 L760 434 L0 434 Z" fill="var(--card-dark)"/>
      <path d="M0 206 C 200 186, 360 286, 520 306 C 640 321, 710 306, 760 296" fill="none" stroke="var(--accent-line)" stroke-width="2"/>
    </svg>

    <div class="front-brand">
      <div class="brand-name">Brindlewood Terrain, LLC</div>
      <div class="brand-tagline">Oil and Gas Land Services</div>
    </div>

    <ul class="contact-list">
      <li>
        <svg class="contact-icon" viewBox="0 0 16 16" aria-hidden="true"><circle cx="8" cy="8" r="8" fill="#f2f2f2"/><path d="M8 3.5a3 3 0 0 0-3 3c0 2.2 3 5.8 3 5.8s3-3.6 3-5.8a3 3 0 0 0-3-3zm0 4.1a1.1 1.1 0 1 1 0-2.2 1.1 1.1 0 0 1 0 2.2z" fill="#3b3b3b"/></svg>
        <span class="contact-lines">426 West Orchard Lane<br>North Canton, OH 44720</span>
      </li>
      <li>
        <svg class="contact-icon" viewBox="0 0 16 16" aria-hidden="true"><circle cx="8" cy="8" r="8" fill="#f2f2f2"/><path d="M5.2 4h1.6l.8 2-1 .8a5 5 0 0 0 2.6 2.6l.8-1 2 .8v1.6c0 .5-.4.9-.9.9A7.5 7.5 0 0 1 4.3 4.9c0-.5.4-.9.9-.9z" fill="#3b3b3b"/></svg>
        <span class="contact-lines">330-555-0148<br>330-555-0192</span>
      </li>
      <li>
        <svg class="contact-icon" viewBox="0 0 16 16" aria-hidden="true"><circle cx="8" cy="8" r="8" fill="#f2f2f2"/><rect x="4" y="5" width="8" height="6" fill="none" stroke="#3b3b3b" stroke-width="1.2"/><path d="M4 5l4 3.3L12 5" fill="none" stroke="#3b3b3b" stroke-width="1.2"/></svg>
        <span class="contact-lines">gavin.r.ressler@quellmail.net</span>
      </li>
    </ul>

    <div class="person">
      <div class="person-name">Gavin Ressler</div>
      <div class="person-title">Petroleum Landman</div>
    </div>
  </section>

</body>
</html>
```